Business Card Design needed Have Logo Files

Hello, I am in need of a business card design.

Company Name: Quartz Traders

Company Address:
2714 E. Palmer Ave
Suite 482B
Eastbrook Falls, Oregon 97415

I think the colors blue, grey, silver (metallic), white, and black are good choices to go with for coloring.

The Owen Pratt and the Copper Sheet are my favorites from the examples so far. Love the bring and edgy blues.

Photo's I have added are designs that I like. I'll also be adding source files.

Logo Source documents have been added.

Project Deadline Extended
Reason: Father passed away and had to take care of his affairs, back in business now.

Need front and back. Try to give it a backside that has a wow factor to it. I've changed the color spectrum to blue, black, purple, and pink for the front side. Think of it as 90% blue and black, 7% purple, 3 % pink when it comes to thinking of ratios of how much of each color i'd like to see on the card. Backside you can use any of those 4 colors as much as you'd like to give it memorable.

Industry/Entity Type

Business

Colors
0492cd
33a6d7
0355a3
3176b5
ffffff
aaaaaa
cbcbcb
9d9d9d
5c5c5c

Requirements
Must have
• Name
Company Address
Work Number
Mobile Number

Doublesided.
Rounded edges

```html
<!DOCTYPE html>
<html lang="en">
<head>
<meta charset="utf-8">
<title>Quartz Traders – Business Card Front and Back</title>
<link rel="stylesheet" href="https://fonts.googleapis.com/css2?family=Tenor+Sans&display=swap">
<style>
  :root {
    --page-bg: #e6e3df;
    --space-blue: #3176b5;
    --space-bright: #33a6d7;
    --space-deep: #0355a3;
    --nebula-grey: #5c5c5c;
    --silver: #cbcbcb;
    --slate: #4a5580;
    --slate-dark: #3c4670;
    --logo-blue: #4fb8f0;
    --text-white: #ffffff;
    --card-shadow: rgba(0, 0, 0, 0.35);
  }
  * { box-sizing: border-box; margin: 0; padding: 0; }
  html, body {
    width: 1200px;
    height: 1200px;
    overflow: hidden;
    background: var(--page-bg);
    font-family: "Tenor Sans", sans-serif;
  }
  .sheet {
    position: relative;
    width: 1200px;
    height: 1200px;
  }
  .card {
    position: absolute;
    left: 160px;
    width: 880px;
    height: 500px;
    border-radius: 28px;
    overflow: hidden;
    box-shadow: 0 10px 30px var(--card-shadow);
  }
  .card--front { top: 60px; }
  .card--back { top: 640px; }

  /* Front */
  .front-artwork {
    position: absolute;
    inset: 0;
    background:
      radial-gradient(ellipse 60% 40% at 38% 35%, rgba(255,255,255,0.85), rgba(255,255,255,0) 70%),
      linear-gradient(135deg, var(--space-deep) 0%, var(--space-blue) 30%, #9fb8e6 50%, #a9adbc 62%, var(--nebula-grey) 100%);
  }
  .front-brand {
    position: absolute;
    left: 0;
    right: 0;
    top: 130px;
    display: flex;
    flex-direction: column;
    align-items: center;
    gap: 44px;
  }
  .brand-mark {
    width: 150px;
    height: 150px;
    border-radius: 50%;
    background: var(--logo-blue);
  }
  .brand-name {
    font-size: 74px;
    letter-spacing: 3px;
    color: var(--logo-blue);
    line-height: 1;
    white-space: nowrap;
  }

  /* Back */
  .back-band {
    position: absolute;
    inset: 0;
    background: linear-gradient(180deg, var(--slate) 0%, var(--slate) 20%, #8e97b8 38%, #ffffff 50%, #8e97b8 62%, var(--slate) 80%, var(--slate-dark) 100%);
  }
  .back-space {
    position: absolute;
    top: 0;
    right: 0;
    width: 250px;
    height: 100%;
    background:
      radial-gradient(circle at 40% 40%, rgba(160,200,255,0.6), rgba(160,200,255,0) 55%),
      linear-gradient(90deg, rgba(74,85,128,0) 0%, var(--space-blue) 18%, var(--space-bright) 60%, var(--space-blue) 100%);
  }
  .back-details {
    position: absolute;
    left: 28px;
    top: 18px;
    width: 590px;
    color: var(--text-white);
  }
  .company-name {
    font-size: 60px;
    line-height: 1.2;
    font-weight: 400;
    white-space: nowrap;
  }
  .person {
    margin-top: 40px;
    font-size: 37px;
    line-height: 1.3;
  }
  .person-role { font-size: 35px; }
  .contact-list {
    margin-top: 54px;
    font-size: 28px;
    line-height: 38px;
    list-style: none;
  }
  .contact-item { display: flex; white-space: nowrap; }
  .contact-label { flex: none; margin-right: 10px; }
</style>
</head>
<body>
<main class="sheet">
  <section class="card card--front" aria-label="Card front">
    <div class="front-artwork" role="img" aria-label="Deep space scene: blue starfield and galaxy on the left, grey nebula on the right"></div>
    <div class="front-brand">
      <span class="brand-mark" aria-hidden="true"></span>
      <span class="brand-name">QUARTZ TRADERS</span>
    </div>
  </section>

  <section class="card card--back" aria-label="Card back">
    <div class="back-band"></div>
    <div class="back-space" role="img" aria-label="Blue starfield nebula with bright stars"></div>
    <div class="back-details">
      <h1 class="company-name">Quartz Traders</h1>
      <p class="person">Owen Pratt<br><span class="person-role">-Owner-</span></p>
      <ul class="contact-list">
        <li class="contact-item"><span class="contact-label">Phone:</span><span>0147 258 369</span></li>
        <li class="contact-item"><span class="contact-label">Mobile:</span><span>9632 587 410</span></li>
        <li class="contact-item"><span class="contact-label">Address:</span><span>2714 E. Palmer Ave, Suite 482B,<br>Eastbrook Falls, Oregon,<br>97415</span></li>
      </ul>
    </div>
  </section>
</main>
</body>
</html>
```